Like us

We need a contest ad that offers a free weekend getaway stay in our Spa Suite- Bridal or Family Suite or King Suite, winners choice. (subject to availability, some conditions apply)
Objective - to encourage existing followers to refer friends and obtain new likes. Each referral "like" should leave a comment with just the referral name in the comment line. We will compile these referral names and the new like names for 1 "referer" weekend getaway package & 1 new "like" weekend getaway package Prize package includes a dinner certificate at the Marlow Hearth (value $ 30) & a complimentary bottle of champagne
(In room or at the Restaurant.) Chatterly Contest closes June 30th, 2014. The professional image is the important part of the design, comment lines can be used for contest explanations, however it would be nice to incorporate in the design. Design first!
The Motel Logo is AR Bonnie with a shadow. (bad copy uploaded)

Target Market(s)

Travelers

Industry/Entity Type

Restaurant

Requirements
Must have
• Professional Image
Nice to have
• Explanation of contest

```html
<!DOCTYPE html>
<html lang="en">
<head>
<meta charset="utf-8">
<title>Win a Weekend Getaway – Refer a Friend</title>
<link href="https://fonts.googleapis.com/css2?family=Aleo:wght@400;500;700&display=swap" rel="stylesheet">
<style>
  :root {
    --page: #ffffff;
    --frame: #2b2b2b;
    --panel: #b4935f;
    --ink: #1f1f1f;
    --light: #ffffff;
    --gold: #f2c230;
    --champagne-dark: #1e1208;
    --champagne-mid: #6b4a22;
    --champagne-light: #e9c98a;
    --room-wall: #cbbfae;
    --room-dark: #4a3a2c;
    --room-warm: #d6a23e;
    --room-deep: #3a2412;
  }
  * { margin: 0; padding: 0; box-sizing: border-box; }
  html, body { width: 1200px; height: 1000px; overflow: hidden; background: var(--page); }
  body { position: relative; font-family: "Aleo", Georgia, serif; color: var(--ink); }

  .frame {
    position: absolute; left: 20px; top: 17px; width: 1163px; height: 966px;
    border: 6px solid var(--frame);
  }

  .photo { position: absolute; }
  .photo--champagne {
    left: 69px; top: 202px; width: 268px; height: 598px;
    background:
      radial-gradient(ellipse at 75% 70%, var(--champagne-light) 0%, rgba(233,201,138,0.4) 25%, transparent 50%),
      linear-gradient(100deg, var(--champagne-dark) 0%, var(--champagne-dark) 45%, var(--champagne-mid) 75%, #3a2510 100%);
  }
  .photo--twin-room {
    left: 722px; top: 202px; width: 411px; height: 295px;
    background: linear-gradient(180deg, #9a9088 0%, var(--room-wall) 30%, #b9ad9c 60%, var(--room-dark) 100%);
  }
  .photo--queen-room {
    left: 722px; top: 506px; width: 411px; height: 294px;
    background:
      radial-gradient(circle at 12% 22%, #f7d77c 0%, transparent 22%),
      radial-gradient(circle at 80% 22%, #f7d77c 0%, transparent 18%),
      radial-gradient(ellipse at 60% 75%, #e8e6e0 0%, transparent 40%),
      linear-gradient(180deg, var(--room-warm) 0%, #8a5a22 55%, var(--room-deep) 100%);
  }

  .offer {
    position: absolute; left: 344px; top: 202px; width: 370px; height: 598px;
    background: var(--panel);
    box-shadow: 2px 2px 4px rgba(0,0,0,0.25);
    text-align: center;
    text-transform: uppercase;
  }
  .offer__title {
    position: absolute; left: 0; top: 16px; width: 100%;
    color: var(--light); font-weight: 500; font-size: 29px; line-height: 28px; letter-spacing: 0.5px;
  }
  .offer__stay {
    position: absolute; left: 0; top: 84px; width: 100%;
    font-size: 12.5px; line-height: 15px;
  }
  .offer__suites {
    position: absolute; left: 0; top: 116px; width: 100%;
    font-size: 18px; line-height: 22px;
  }
  .divider {
    position: absolute; left: 37px; width: 293px; height: 3px; background: var(--ink);
  }
  .divider--labelled { top: 173px; }
  .divider__label {
    position: absolute; left: 50%; top: -7px; transform: translateX(-50%);
    background: var(--panel); padding: 0 9px;
    color: var(--light); font-size: 12px; line-height: 15px; font-weight: 500;
  }
  .offer__includes {
    position: absolute; left: 0; top: 190px; width: 100%;
    font-size: 17.5px; line-height: 21px;
  }
  .offer__includes small { display: block; font-size: 9px; line-height: 12px; }
  .divider--top { top: 297px; }
  .divider--bottom { top: 432px; }
  .offer__headline {
    position: absolute; left: 0; top: 305px; width: 100%;
    font-size: 66px; line-height: 59px; font-weight: 400;
  }
  .offer__headline span { display: block; letter-spacing: 1px; }
  .offer__headline span + span { letter-spacing: 8px; }
  .offer__how {
    position: absolute; left: 37px; top: 448px; width: 293px;
    color: var(--light); font-size: 18.5px; line-height: 22.5px; font-weight: 500;
    letter-spacing: 0.5px;
  }
  .offer__how span {
    display: block; white-space: nowrap;
    text-align: justify; text-align-last: justify;
  }
  .offer__terms {
    position: absolute; left: 0; top: 570px; width: 100%;
    text-transform: none; font-size: 10px; line-height: 12px;
  }

  .brand { position: absolute; font-family: "Aleo", Georgia, serif; }
  .brand--motel {
    left: 900px; top: 746px; width: 154px;
    color: var(--gold); font-weight: 700; text-align: right;
  }
  .brand--motel .brand__name { display: block; font-size: 21px; line-height: 26px; }
  .brand--motel .brand__kind { display: block; font-size: 11px; line-height: 14px; text-transform: uppercase; letter-spacing: 1px; }
  .brand--grill {
    left: 1062px; top: 712px; width: 60px; height: 80px; background: var(--light);
    display: flex; align-items: center; justify-content: center; text-align: center;
    font-size: 12px; line-height: 14px; font-weight: 700; color: var(--ink);
  }
</style>
</head>
<body>
  <div class="frame"></div>

  <div class="photo photo--champagne" role="img" aria-label="Bottle of champagne with two filled champagne flutes in warm light"></div>

  <section class="offer">
    <h1 class="offer__title">Win a weekend<br>getaway!</h1>
    <p class="offer__stay">Free one weekend stay in<br>winners choice:</p>
    <p class="offer__suites">King Suite • Spa Suite<br>Bridal Suite • Family Suite</p>
    <div class="divider divider--labelled"><span class="divider__label">Includes</span></div>
    <p class="offer__includes">
      $30 value dinner certificate<br>at the Marlow Hearth
      <small>and</small>
      Complimentary bottle of<br>champagne
    </p>
    <div class="divider divider--top"></div>
    <h2 class="offer__headline"><span>Refer a</span><span>Friend</span></h2>
    <div class="divider divider--bottom"></div>
    <p class="offer__how">
      <span>Refer our Chatterly page</span>
      <span>to a friend and have</span>
      <span>them like &amp; comment</span>
      <span>mentioning your name</span>
      <span>for a chance to win!</span>
    </p>
    <p class="offer__terms">Contest Ends: June 30th, 2014<br>*Subject to availability. Conditions may apply.</p>
  </section>

  <div class="photo photo--twin-room" role="img" aria-label="Motel room with two beds, armchairs and a desk lamp"></div>
  <div class="photo photo--queen-room" role="img" aria-label="Motel room with a made bed between two glowing bedside lamps"></div>

  <div class="brand brand--motel"><span class="brand__name">Bramwell's</span><span class="brand__kind">Motel</span></div>
  <div class="brand brand--grill">Marlow<br>Hearth</div>
</body>
</html>
```